Homebuilder & Remodeling Firm looking for archectrual looking website

We are a Custom home building & remodeling company since 1986 and would like to launch a website.Carl Tondevik the principle of the firm is a graduate of Harwell Univesity school of architecture and draws his own designs and working drawings. and has done many residential, single and multi family projects in the Dallas Ft Worth Metroplex. We want our website to be architectural in design and visually appealing. We will eventually have photos to provide for you. The message we want to communicate is we have current update knowledge with trends, and longevity in experience. Our message is that we are a firm that designs and remodels fully through and we provide a well executed custom home that is unique to each client. The Homes that we build are unique ,authentic and sustainable architectural styles such as mid century modern, contemporary, transitional and they are sophisticated homes to compliment individual lifestyles of our clients. We have a passion for construction and an attention to detail that makes your dreams come to life. We listen to each clients every need in functionality and form and take them from pre-construction to post-construction follow -up.
We help you invest in your home. Thoughts Create Reality

EXAMPLES OF WEBSITES THAT WE LIKE. PLEASE DO
MORE CONTEMPORARY, SLEEK, ARCHITECTURAL

* Please make the LOGO a bigger part of design

http://pellamcrew.build/
https://www.vintrasol.co/
http://dostavanehomes.com/
http://www.milesfardowdesign.com/
http://www.quillmerton.com/
http://fennikdesignstudios.com/about
http://brandelorgc.com/

thank you,

Reason: We have many clients asking to see our website and re ready to launch something for them to look at

Target Market(s)

Home owners, home buyers, interior designers, All ages

Industry/Entity Type

Builders

Coding

Coded - Design and coding required

Number of Pages Required

5+ page

Font styles to use
Sans Serif

Requirements
Must have
• HTML5 OR PHP
• graphic artist must speak English:
• *Visually appealing, user friendly,
• * the website should reflect the stability and integrity of the company since it has been in business for over 30 years
• * a sophistication and refinement is our mandate.
Should not have
• Too busy, too much going on, we want more minimal in design and artsitic

```html
<!DOCTYPE html>
<html lang="en">
<head>
<meta charset="utf-8">
<title>Tondevik Development</title>
<link href="https://fonts.googleapis.com/css2?family=Montserrat:wght@400;500;600&family=Raleway:wght@400;500;600&display=swap" rel="stylesheet">
<style>
:root{
  --navy:#0b2a63;
  --navy-light:#8fa6d6;
  --ink:#1b1b1b;
  --muted:#6d6d6d;
  --line:#e4e4e4;
  --side:#f7f7f7;
  --paper:#ffffff;
  --soft:#f3f3f3;
  --footer:#141414;
}
*{margin:0;padding:0;box-sizing:border-box}
html,body{width:1200px;height:3455px;overflow:hidden;background:var(--paper)}
body{position:relative;font-family:"Raleway",sans-serif;color:var(--ink)}
.abs{position:absolute}
h1,h2,h3{font-weight:400}

/* sidebar */
.sidebar{position:absolute;left:0;top:0;width:293px;height:3455px;background:var(--side);border-right:1px solid #ececec}
.brand{position:absolute;top:62px;left:0;width:293px;text-align:center;font-family:"Montserrat",sans-serif;font-weight:500;font-size:33px;line-height:42px;color:var(--navy);letter-spacing:.5px}
.nav{position:absolute;top:172px;left:18px;width:257px;list-style:none}
.nav li{height:50px;line-height:50px;text-align:center;font-family:"Montserrat",sans-serif;font-size:11px;letter-spacing:3px;color:#9a9a9a;border-bottom:1px solid var(--line)}
.social{position:absolute;top:522px;left:0;width:293px;display:flex;justify-content:center;gap:22px}
.social span{width:14px;height:14px;border-radius:50%;background:#8d8d8d;display:block}

/* hero */
.hero{left:293px;top:0;width:907px;height:567px;background:linear-gradient(100deg,#efefef 0%,#fafafa 45%,#e9ecef 70%,#f6f7f8 100%)}
.hero-title{position:absolute;left:293px;top:262px;width:907px;text-align:center;font-family:"Montserrat",sans-serif;font-weight:500;font-size:36px;letter-spacing:7px;color:var(--navy)}

/* about */
.about{left:293px;top:567px;width:907px;height:552px;background:var(--soft)}
.about-photo{left:293px;top:571px;width:393px;height:514px;background:linear-gradient(160deg,#6a3a26 0%,#3a2318 35%,#d9d3cc 60%,#1b1613 100%)}
.about-head{left:767px;top:665px;font-family:"Montserrat",sans-serif;font-weight:400;font-size:23px;line-height:32px;letter-spacing:1px;color:var(--ink)}
.about-lead{left:767px;top:772px;width:350px;font-size:14px;line-height:21px;color:#333}
.about-body{left:767px;top:876px;width:350px;font-size:11px;line-height:19px;color:var(--muted)}

/* services */
.section-title{left:293px;top:1176px;width:907px;text-align:center;font-family:"Montserrat",sans-serif;font-weight:400;font-size:27px;color:var(--ink)}
.divider{left:463px;top:1243px;width:567px;height:1px;background:#d8d8d8}
.divider-dot{left:751px;top:1246px;width:5px;height:5px;background:var(--ink);border-radius:50%}
.service-photo{top:1313px;width:370px;height:177px}
.service-photo.residential{left:368px;background:linear-gradient(120deg,#e9e6df 0%,#b99f78 50%,#5a4632 100%)}
.service-photo.office{left:767px;background:linear-gradient(120deg,#c25a1c 0%,#e7a35a 40%,#d8dcd6 70%,#6f7d64 100%)}
.service-name{top:1518px;font-family:"Montserrat",sans-serif;font-size:15px;color:var(--ink)}
.service-name b{color:var(--navy);font-weight:600}
.service-text{top:1548px;width:370px;font-size:11px;line-height:19px;color:var(--muted)}

/* bands */
.band{left:293px;width:907px;height:142px;background:var(--navy)}
.btn{width:207px;height:33px;border:1.5px solid #fff;color:#fff;font-family:"Montserrat",sans-serif;font-weight:600;font-size:11px;letter-spacing:1.5px;display:flex;align-items:center;justify-content:center;gap:10px}

/* filter */
.filters{left:293px;top:1854px;width:907px;height:76px;background:var(--paper)}
.filter{top:1880px;height:24px;line-height:24px;font-family:"Montserrat",sans-serif;font-size:9.5px;letter-spacing:2.5px;color:#8a8a8a}
.filter.active{background:var(--navy);color:#fff;padding:0 18px;font-weight:600}

/* grid */
.tile{width:302px;height:204px}

/* testimonials */
.testimonials{left:293px;top:2480px;width:907px;height:555px;background:linear-gradient(135deg,#3a2d22 0%,#5b4a3a 40%,#2e261f 70%,#4a3a2b 100%)}
.testimonials-title{left:293px;top:2538px;width:907px;text-align:center;font-family:"Montserrat",sans-serif;font-weight:500;font-size:26px;color:#fff}
.quote-card{top:2671px;height:272px;background:rgba(30,24,20,.72)}
.quote-mark{width:46px;height:46px;background:var(--navy)}
.quote-text{width:290px;font-size:14px;line-height:22.5px;color:#fff}
.quote-name{height:28px;line-height:28px;padding:0 12px;background:#0d0d0d;font-size:12px;color:var(--navy-light)}
.dot{top:2957px;width:5px;height:5px;border-radius:50%;background:#cfcfcf}

/* footer */
.footer{left:293px;top:3035px;width:907px;height:420px;background:var(--footer)}
.footer-about{left:368px;top:3136px;width:370px;font-size:11px;line-height:20px;color:#d8d8d8}
.contact-title{left:767px;top:3096px;font-family:"Montserrat",sans-serif;font-weight:600;font-size:16px;color:#fff}
.contact-addr{left:767px;top:3134px;font-size:11px;color:#cfcfcf}
.contact-row{left:767px;width:374px;height:40px;border-bottom:1px solid #2c2c2c;font-size:11px;color:#cfcfcf;display:flex;align-items:center}
.contact-row em{font-style:normal;color:var(--navy-light);width:50px}
.copyright{left:368px;top:3404px;font-size:11px;color:#d0d0d0}
.footer-social{left:979px;top:3406px;display:flex;gap:21px}
.footer-social span{width:11px;height:11px;border-radius:50%;background:#e0e0e0;display:block}
</style>
</head>
<body>

<aside class="sidebar">
  <div class="brand">TONDEVIK<br>DEVELOPMENT</div>
  <ul class="nav">
    <li>HOME</li><li>SERVICES</li><li>PROJECTS</li><li>ABOUT</li><li>BLOG</li><li>CONTACT</li>
  </ul>
  <div class="social"><span></span><span></span><span></span><span></span><span></span></div>
</aside>

<div class="abs hero" role="img" aria-label="Bright living room with tall windows and pendant lamps"></div>
<h1 class="hero-title">TONDEVIK DEVELOPMENT</h1>

<section>
  <div class="abs about"></div>
  <div class="abs about-photo" role="img" aria-label="Interior corner with brick wall and dark decorative vases"></div>
  <h2 class="abs about-head">HOME OF CUSTOM<br>REMODELING</h2>
  <p class="abs about-lead">Interior design is the art or process of designing the interior, often including the exterior, of a room or building. An interior designer is someone who coordinates and manages such projects.</p>
  <p class="abs about-body">Interior design is a multifaceted profession that includes conceptual development, communicating with the stakeholders of a project and the management and execution of the design. Lorem ipsum dolor sit amet, consectetur adipisicing elit, sed do eiusmod tempor incididunt ut labore et dolore magna aliqua. Ut enim ad minim veniam, quis nostrud exercitation ullamco laboris nisi ut aliquip ex ea commodo consequat.</p>
</section>

<section>
  <h2 class="abs section-title">What We Do</h2>
  <div class="abs divider"></div>
  <div class="abs divider-dot"></div>
  <div class="abs service-photo residential" role="img" aria-label="Residential living room with lounge chair and bookshelves"></div>
  <div class="abs service-photo office" role="img" aria-label="Office interior with wooden staircase"></div>
  <div class="abs service-name" style="left:376px"><b>Residential</b>&nbsp;&nbsp;Design</div>
  <div class="abs service-name" style="left:767px"><b>Office</b>&nbsp;&nbsp;Design</div>
  <p class="abs service-text" style="left:368px">Sed ut perspiciatis unde omnis iste natus error sit voluptatem accusantium doloremque laudantium, totam rem aperiam, eaque ipsa quae ab illo inventore veritatis et quasi architecto beatae vitae dicta sunt explicabo. Nemo enim ipsam voluptatem quia voluptas sit aspernatur aut odit aut fugit, sed quia</p>
  <p class="abs service-text" style="left:767px">Sed ut perspiciatis unde omnis iste natus error sit voluptatem accusantium doloremque laudantium, totam rem aperiam, eaque ipsa quae ab illo inventore veritatis et quasi architecto beatae vitae dicta sunt explicabo. Nemo enim ipsam voluptatem quia voluptas sit aspernatur aut odit aut fugit, sed quia</p>
</section>

<div class="abs band" style="top:1711px"></div>
<div class="abs btn" style="left:650px;top:1767px">VIEW PORTFOLIO
  <svg width="8" height="10" viewBox="0 0 8 10"><path d="M2 1l4 4-4 4" fill="none" stroke="#fff" stroke-width="1.8"/></svg></div>

<div class="abs filters"></div>
<div class="abs filter active" style="left:435px">ALL PROJECT</div>
<div class="abs filter" style="left:594px">COMMERCIAL</div>
<div class="abs filter" style="left:735px">HOSPITALY</div>
<div class="abs filter" style="left:857px">OFFICE</div>
<div class="abs filter" style="left:953px">RESIDENTIAL</div>

<div class="abs tile" style="left:293px;top:1930px;background:linear-gradient(120deg,#e4e1da,#a88a62 60%,#4b3b2a)" role="img" aria-label="Living room with wooden lounge chair"></div>
<div class="abs tile" style="left:595px;top:1930px;background:linear-gradient(120deg,#6b6259,#d9d3ca 55%,#2a2420)" role="img" aria-label="Hotel bedroom with white bed"></div>
<div class="abs tile" style="left:897px;top:1930px;background:linear-gradient(160deg,#dfe6ea,#9aa3a8 50%,#2b2624)" role="img" aria-label="Glass-roofed lounge with dark armchairs"></div>
<div class="abs tile" style="left:293px;top:2134px;background:linear-gradient(120deg,#2a2521,#8a7866 50%,#d6cfc3)" role="img" aria-label="Modern bedroom with low bed"></div>
<div class="abs tile" style="left:595px;top:2134px;background:linear-gradient(140deg,#5a5b5d,#b9babb 55%,#3c3c3e)" role="img" aria-label="Office meeting room with hexagon wall"></div>
<div class="abs tile" style="left:897px;top:2134px;background:linear-gradient(120deg,#c9a26d,#8a5a31 50%,#3b2516)" role="img" aria-label="Restaurant interior with wooden ceiling"></div>

<div class="abs band" style="top:2338px"></div>
<div class="abs btn" style="left:643px;top:2390px">VIEW ALL PROJECT
  <svg width="8" height="10" viewBox="0 0 8 10"><path d="M2 1l4 4-4 4" fill="none" stroke="#fff" stroke-width="1.8"/></svg></div>

<section>
  <div class="abs testimonials" role="img" aria-label="Dim interior room behind the testimonials"></div>
  <h2 class="abs testimonials-title">Customer Says</h2>

  <div class="abs quote-card" style="left:352px;width:387px"></div>
  <div class="abs quote-mark" style="left:384px;top:2688px"><svg width="46" height="46" viewBox="0 0 46 46"><path d="M16 19h6v6l-3 5h-3l2-5h-2zM25 19h6v6l-3 5h-3l2-5h-2z" fill="#fff"/></svg></div>
  <p class="abs quote-text" style="left:453px;top:2692px;width:272px">I have very much enjoyed with your services. Lorem ipsum dolor sit amet, consectetur adipisicing elit, sed do eiusmod tempor incididunt ut labore et dolore magna aliqua. Ut enim ad minim veniam, quis nostrud exercitation ullamco laboris nisi ut aliquip.</p>
  <div class="abs quote-name" style="left:453px;top:2891px">Owen, Customer</div>

  <div class="abs quote-card" style="left:767px;width:359px"></div>
  <div class="abs quote-mark" style="left:767px;top:2688px"><svg width="46" height="46" viewBox="0 0 46 46"><path d="M16 19h6v6l-3 5h-3l2-5h-2zM25 19h6v6l-3 5h-3l2-5h-2z" fill="#fff"/></svg></div>
  <p class="abs quote-text" style="left:837px;top:2692px;width:260px">I totally recommend your services. Lorem ipsum dolor sit amet, consectetur adipisicing elit, sed do eiusmod tempor incididunt ut labore et dolore magna aliqua. Ut enim ad minim veniam, quis nostrud exercitation ullamco laboris nisi ut aliquip.</p>
  <div class="abs quote-name" style="left:837px;top:2891px">Marcus, Customer</div>

  <div class="abs dot" style="left:742px"></div>
  <div class="abs dot" style="left:756px;background:#8a8a8a"></div>
</section>

<footer>
  <div class="abs footer"></div>
  <p class="abs footer-about">We are team based on Brooklyn. Our expertise on Interior Design. Sed ut perspiciatis unde omnis iste natus error sit voluptatem accusantium doloremque laudantium, totam rem aperiam, eaque ipsa quae ab illo inventore veritatis et quasi architecto beatae vitae dicta sunt explicabo.</p>
  <h3 class="abs contact-title">Contact Us</h3>
  <p class="abs contact-addr">210 Elmwood Center, Dallas</p>
  <div class="abs contact-row" style="top:3154px"><em>Phone</em>(008) 555 0142</div>
  <div class="abs contact-row" style="top:3194px"><em>Fax</em>(008) 555 0142</div>
  <div class="abs contact-row" style="top:3234px"><em>Email</em>contact@tondevikdev.net</div>
  <div class="abs contact-row" style="top:3274px"><em>Web</em>http://tondevikdev.net/</div>
  <p class="abs copyright">© Copyright 2017 - Tondevik Development</p>
  <div class="abs footer-social"><span></span><span></span><span></span><span></span><span></span></div>
</footer>

</body>
</html>
```